BrevoLunt Business Card Design Project

We are looking for a modern, clean business card design for our new company. We are a consulting firm focused on the financial services market providing management and IT consulting to banks, insurance companies, etc. Please include our company logo and company contact information from the attached file in the design. Two versions of the logo are attached, either version is acceptable. Logos are available in other file formats if needed. We would like to include the contact information for both our UK and US offices as well as the following information for each individual card holder: Name, position/title, address, phone number and e-mail address.
Updates
Project Deadline Extended
Reason: A last minute trip over seas has prevented us from finalizing the decision. A decision will be made this week. We apologize for the inconvenience.
Industry/Entity Type
Business
Contact Information for Business Card
Company logo.
Company locations and phone numbers for both the US and UK offices.
Company URL.
Cardholder Name
Cardholder Position/title
Cardholder Address
Cardholder Phone Number
Cardholder e-mail Address
Look and feel
Each slider illustrates characteristics of the customer's brand and the style your logo design should communicate.

```html
<!DOCTYPE html>
<html lang="en">
<head>
<meta charset="utf-8">
<title>BrevoLunt Partners – Business Card</title>
<link rel="stylesheet" href="https://fonts.googleapis.com/css2?family=Tinos:ital,wght@0,400;0,700;1,400;1,700&display=swap">
<style>
  :root {
    --stage: #2b2b2b;
    --blue-top: #3d5c92;
    --blue-bottom: #17233c;
    --grey-light: #9c9c9c;
    --grey-mid: #6f6f6f;
    --grey-dark: #3a3a3a;
    --panel-top: #878787;
    --panel-bottom: #595959;
    --ink: #111111;
    --ink-soft: #1e1e1e;
    --navy: #1f3560;
    --brand-blue: #2f4f86;
    --white: #ffffff;
    --icon-bg: #4a4a4a;
  }
  * { margin: 0; padding: 0; box-sizing: border-box; }
  html, body { width: 1200px; height: 675px; overflow: hidden; background: var(--stage); }
  body { position: relative; font-family: "Tinos", "Times New Roman", serif; }

  .card {
    position: absolute;
    left: 322px;
    width: 556px;
    height: 268px;
    overflow: hidden;
    box-shadow: 0 4px 12px rgba(0,0,0,0.55);
  }
  .card--back { top: 47px; }
  .card--front { top: 361px; background: var(--white); }
  .card__shapes { position: absolute; inset: 0; width: 556px; height: 268px; }

  .abs { position: absolute; white-space: nowrap; }

  /* Back side */
  .addresses__heading { left: 76px; top: 37px; font-size: 14px; font-weight: 700; font-style: italic; color: var(--ink); }
  .addresses__line { width: 160px; left: 67px; text-align: center; font-size: 11px; font-style: italic; color: var(--ink-soft); }
  .phones__heading { left: 324px; top: 101px; font-size: 12.5px; font-weight: 700; font-style: italic; color: var(--ink); }
  .phones__row { left: 344px; font-size: 10.5px; font-style: italic; color: var(--ink-soft); }
  .phones__country { display: inline-block; width: 32px; }
  .website { left: 336px; top: 241px; font-size: 12.5px; font-weight: 700; font-style: italic; color: var(--ink); }

  /* Front side */
  .brand { left: 22px; top: 20px; display: flex; align-items: center; gap: 10px; }
  .brand__square { width: 22px; height: 22px; background: var(--grey-mid); }
  .brand__name { font-size: 26px; font-weight: 700; color: var(--brand-blue); line-height: 1; }
  .holder__bar { left: 0; top: 154px; width: 6px; height: 42px; background: var(--grey-dark); }
  .holder__name { left: 14px; top: 170px; font-size: 14.5px; font-weight: 700; font-style: italic; color: var(--navy); letter-spacing: 0.2px; }
  .holder__title { left: 14px; top: 184px; font-size: 10.5px; font-style: italic; color: var(--ink); }
  .contact { left: 248px; display: flex; align-items: center; gap: 12px; font-size: 12.5px; font-style: italic; color: var(--ink); }
  .contact__icon { width: 20px; height: 20px; }
</style>
</head>
<body>

<section class="card card--back" aria-label="Business card, back">
  <svg class="card__shapes" viewBox="0 0 556 268" aria-hidden="true">
    <defs>
      <linearGradient id="backBlue" x1="0" y1="0" x2="0" y2="1">
        <stop offset="0" stop-color="var(--blue-top)"/>
        <stop offset="1" stop-color="var(--blue-bottom)"/>
      </linearGradient>
      <linearGradient id="backGrey" x1="0" y1="0" x2="0" y2="1">
        <stop offset="0" stop-color="var(--grey-light)"/>
        <stop offset="0.55" stop-color="var(--grey-mid)"/>
        <stop offset="1" stop-color="var(--grey-dark)"/>
      </linearGradient>
      <linearGradient id="divider" x1="0" y1="0" x2="0" y2="1">
        <stop offset="0" stop-color="var(--blue-top)" stop-opacity="0.4"/>
        <stop offset="0.5" stop-color="var(--blue-top)"/>
        <stop offset="1" stop-color="var(--blue-top)" stop-opacity="0.4"/>
      </linearGradient>
    </defs>
    <rect width="556" height="268" fill="url(#backBlue)"/>
    <path d="M0 0 H478 Q498 0 503 20 L556 268 H80 Q58 268 50 246 Z" fill="url(#backGrey)"/>
    <path d="M276 45 L278 142 L276 240 L274 142 Z" fill="url(#divider)"/>
  </svg>

  <h2 class="abs addresses__heading">Company Addresses:</h2>
  <p class="abs addresses__line" style="top:66px">418 N Cobble Ave, Suite</p>
  <p class="abs addresses__line" style="top:85px">204-117</p>
  <p class="abs addresses__line" style="top:104px">Lakeview UT 84060</p>
  <p class="abs addresses__line" style="top:123px">United States</p>
  <p class="abs addresses__line" style="top:149px">14-16 Harrow Mews</p>
  <p class="abs addresses__line" style="top:168px">London</p>
  <p class="abs addresses__line" style="top:186px">E2 9QL</p>
  <p class="abs addresses__line" style="top:205px">Great Britain</p>

  <h2 class="abs phones__heading">Company Phone Numbers:</h2>
  <p class="abs phones__row" style="top:120px"><span class="phones__country">US</span>(801) 555-0147</p>
  <p class="abs phones__row" style="top:137px"><span class="phones__country">UK</span>+44 7700 900482</p>

  <p class="abs website">www.brevoluntpartners.com</p>
</section>

<section class="card card--front" aria-label="Business card, front">
  <svg class="card__shapes" viewBox="0 0 556 268" aria-hidden="true">
    <defs>
      <linearGradient id="frontBlue" x1="0" y1="0" x2="0" y2="1">
        <stop offset="0" stop-color="var(--blue-top)"/>
        <stop offset="1" stop-color="var(--blue-bottom)"/>
      </linearGradient>
      <linearGradient id="frontPanel" x1="0" y1="0" x2="0" y2="1">
        <stop offset="0" stop-color="var(--panel-top)"/>
        <stop offset="1" stop-color="var(--panel-bottom)"/>
      </linearGradient>
    </defs>
    <polygon points="303,0 556,0 556,268 432,268" fill="url(#frontBlue)"/>
    <path d="M220 83 H474 Q490 83 494 99 L523 220 Q526 232 512 232 H250 Q234 232 231 218 L206 97 Q204 83 220 83 Z" fill="url(#frontPanel)"/>
  </svg>

  <div class="abs brand">
    <span class="brand__square" aria-hidden="true"></span>
    <span class="brand__name">BrevoLunt Partners</span>
  </div>

  <span class="abs holder__bar" aria-hidden="true"></span>
  <h1 class="abs holder__name">CARDHOLDER NAME</h1>
  <p class="abs holder__title">Cardholder Position/title</p>

  <p class="abs contact" style="top:115px">
    <svg class="contact__icon" viewBox="0 0 20 20" aria-hidden="true">
      <circle cx="10" cy="10" r="10" fill="var(--icon-bg)"/>
      <path d="M6.5 5.5 L8.3 5.2 L9.2 7.6 L8.1 8.5 Q9.1 10.7 11.4 11.9 L12.3 10.8 L14.7 11.7 L14.4 13.5 Q9.8 14 6.5 5.5 Z" fill="var(--grey-light)"/>
    </svg>
    Cardholder Phone Number
  </p>
  <p class="abs contact" style="top:146px">
    <svg class="contact__icon" viewBox="0 0 20 20" aria-hidden="true">
      <circle cx="10" cy="10" r="10" fill="var(--icon-bg)"/>
      <rect x="5" y="6.5" width="10" height="7" fill="var(--grey-light)"/>
      <path d="M5 6.5 L10 10.5 L15 6.5" fill="none" stroke="var(--icon-bg)" stroke-width="1"/>
    </svg>
    Cardholder e-mail Address
  </p>
  <p class="abs contact" style="top:177px">
    <svg class="contact__icon" viewBox="0 0 20 20" aria-hidden="true">
      <circle cx="10" cy="10" r="10" fill="var(--icon-bg)"/>
      <path d="M10 15.5 Q6.5 11 6.5 8.5 A3.5 3.5 0 0 1 13.5 8.5 Q13.5 11 10 15.5 Z" fill="var(--grey-light)"/>
      <circle cx="10" cy="8.5" r="1.3" fill="var(--icon-bg)"/>
    </svg>
    Cardholder address
  </p>
</section>

</body>
</html>
```